Derek Osei Consulting

I've the wording, and the rough layout. See attached MicroSoft Word File. I need a professional to make my postcard "look pretty".

Industry/Entity Type

Consulting

```html
<!DOCTYPE html>
<html lang="en">
<head>
<meta charset="utf-8">
<title>Derek Osei Consulting – Postcard</title>
<link href="https://fonts.googleapis.com/css2?family=Arimo:wght@400;700&display=swap" rel="stylesheet">
<style>
  :root {
    --ink-blue: #3a4ea6;
    --panel-green: #6abf4b;
    --paper: #ffffff;
    --text-light: #ffffff;
    --rule-grey: #c8c8c8;
    --stamp-grey: #bdbdbd;
  }
  html, body {
    margin: 0;
    padding: 0;
    overflow: hidden;
    background: var(--paper);
  }
  .postcard {
    position: relative;
    width: 1200px;
    height: 776px;
    background: var(--paper);
    font-family: "Arimo", Arial, sans-serif;
    overflow: hidden;
  }
  .headline {
    position: absolute;
    left: 31px;
    top: 19px;
    margin: 0;
    font-size: 27.2px;
    font-weight: 400;
    color: var(--ink-blue);
    white-space: nowrap;
  }
  .message-panel {
    position: absolute;
    left: 0;
    top: 72px;
    width: 796px;
    height: 597px;
    background: var(--panel-green);
    color: var(--text-light);
    box-sizing: border-box;
    padding: 19px 30px 0 31px;
  }
  .secrets-list {
    list-style: none;
    margin: 0;
    padding: 0;
    font-size: 19.3px;
    line-height: 29px;
    width: 700px;
  }
  .secrets-list .num {
    display: inline-block;
    width: 33px;
  }
  .question {
    margin: 21px 0 0;
    font-size: 23.2px;
    font-weight: 700;
    line-height: 30px;
  }
  .answer {
    margin: 31px 0 0;
    font-size: 19.3px;
    line-height: 29px;
    width: 728px;
  }
  .turn-over {
    margin: 8px 0 0;
    font-size: 19.3px;
    font-weight: 700;
    line-height: 29px;
    padding-left: 141px;
  }
  .stamp-box {
    position: absolute;
    left: 1030px;
    top: 46px;
    width: 140px;
    height: 145px;
    border: 1px solid var(--stamp-grey);
    box-sizing: border-box;
  }
  .address-lines {
    position: absolute;
    left: 808px;
    top: 386px;
    width: 362px;
  }
  .address-lines span {
    display: block;
    height: 46px;
    border-top: 1px solid var(--rule-grey);
    box-sizing: border-box;
  }
  .website {
    position: absolute;
    left: 42px;
    top: 701px;
    margin: 0;
    font-size: 23px;
    font-weight: 700;
    color: var(--ink-blue);
  }
</style>
</head>
<body>
<div class="postcard">
  <h1 class="headline">Learn the small-business know-how only “insiders” know</h1>

  <section class="message-panel">
    <ol class="secrets-list">
      <li><span class="num">1.</span>How to make people want to have what you have for sale?</li>
      <li><span class="num">2.</span>How to turn new customers into repeat customers?</li>
      <li><span class="num">3.</span>How to make repeat customers comeback more often?</li>
      <li><span class="num">4.</span>How to spend less time with each customer, yet increase your profit on each business transaction?</li>
      <li><span class="num">5.</span>How to get more operating capital?</li>
      <li><span class="num">6.</span>How to buy low and sell high?</li>
      <li><span class="num">7.</span>How to manage employees and contractors?</li>
      <li><span class="num">8.</span>Which marketing methods are total waste of time and money?</li>
    </ol>
    <h2 class="question">Why do 80% of all businesses fail???</h2>
    <p class="answer">Because their owners didn’t know what “business insiders” know. They worked very long hours, they had a lot of stresses and headaches, and in the end, due to their lack of business know-how, their businesses failed and they were left with a bunch of debt, a broken heart and sometimes a broken family too. Don’t become one of them! Become a real “insider”, run a successful business without stress and enjoy life! To find out more:</p>
    <p class="turn-over">Turn to the other side for more info -&gt;</p>
  </section>

  <div class="stamp-box" aria-label="Stamp area"></div>

  <div class="address-lines" aria-label="Address lines">
    <span></span><span></span><span></span><span></span><span></span><span></span>
  </div>

  <p class="website">www.InsiderBizKnowHow.com</p>
</div>
</body>
</html>
```